Homepage for a Workout + Food Tracking Mobile App

We need a design for the homepage of our workout and food tracking app called FitBrook (working name, most likely not finalized). The app has many uses, namely a "Strength Review", food logging, workout tracking, statistics/analytics, an AI powered form review tool and an ability to ask an AI any workout, nutrition or app related questions. The homepage should feature some way to access the above listed features as well as an outline, 3d design, diagram or any other way to represent the human body split up into muscle groups for the user to see what muscles they've hit in any amount of time. There should be a section for a profile picture, username, "trophy case" with room for ideally 3 small "trophy" icons.
The main colour should be gold/dark yellow (I used #DEA30A) but I am very flexible on that and I'm curious to try out other colours. The background colour I am also flexible on, I went with a dark gray.
The screenshot I uploaded is in no way what your design needs to look like. Use it more to check what buttons and elements should be present.
I'll likely need more designs for other screens in the future and will be happy to work further with the designer chosen.
Target Market(s)
Gymgoers, People on a diet, Weightlifters,
Look and feel

```html
<!DOCTYPE html>
<html lang="en">
<head>
<meta charset="utf-8">
<title>FitBrook – Home Screen Variants</title>
<link href="https://fonts.googleapis.com/css2?family=Poppins:wght@400;500;600;700&display=swap" rel="stylesheet">
<style>
  :root{
    --canvas-top:#1f3a6c;
    --canvas-bottom:#2796bd;
    --header-a:#1b6fd0;
    --header-b:#1a9bbd;
    --surface:#151a28;
    --panel:#1c2335;
    --frame:#0b0f1a;
    --accent:#1e9bff;
    --accent-soft:#1aa3ff;
    --muscle:#1f8fff;
    --muscle-deep:#0f5fc4;
    --body-dark:#0c1222;
    --text:#ffffff;
    --muted:#8c96ab;
    --green:#47d16b;
    --purple:#9a5bff;
    --red:#ff3d57;
  }
  *{box-sizing:border-box;margin:0;padding:0}
  html,body{width:837px;height:1200px;overflow:hidden}
  body{
    font-family:"Poppins",sans-serif;
    background:linear-gradient(180deg,var(--canvas-top),var(--canvas-bottom));
    display:flex;align-items:center;justify-content:center;
  }
  .variants{display:flex;gap:18px;align-items:center}
  .variant{display:flex;align-items:flex-end;gap:8px}
  .variant-label{
    writing-mode:vertical-rl;transform:rotate(180deg);
    color:var(--accent-soft);font-size:8px;font-weight:500;letter-spacing:4px;
    width:14px;white-space:nowrap;margin-bottom:10px;
  }
  .phone{
    position:relative;width:230px;height:498px;border-radius:34px;
    border:5px solid var(--frame);background:var(--surface);overflow:hidden;
  }
  .screen{position:absolute;inset:0}
  .header{
    position:absolute;left:0;top:0;width:100%;height:140px;
    background:linear-gradient(180deg,var(--header-a),var(--header-b));
    border-radius:0 0 50% 50% / 0 0 22px 22px;
  }
  .status{position:absolute;top:9px;left:18px;right:16px;display:flex;justify-content:space-between;color:var(--text);font-size:8.5px;font-weight:600}
  .status-icons{display:flex;gap:3px;align-items:center}
  .status-icons span{display:block;background:var(--text);border-radius:1px}
  .greeting{
    position:absolute;top:26px;left:8px;width:206px;height:58px;border-radius:30px;
    background:rgba(12,34,78,.45);box-shadow:inset 0 1px 0 rgba(255,255,255,.12);
  }
  .avatar{position:absolute;left:6px;top:6px;width:46px;height:46px;border-radius:50%;
    background:radial-gradient(circle at 40% 40%,#7f9bb0,#3e4f5c);border:2px solid rgba(255,255,255,.35)}
  .hello{position:absolute;left:64px;top:8px;font-size:8.5px;color:#cfe3ff}
  .hello b{color:var(--text);font-weight:600}
  .trophies{position:absolute;left:64px;top:25px;display:flex;gap:12px}
  .trophy{width:14px;height:24px;border-radius:3px 3px 2px 2px;background:linear-gradient(180deg,rgba(255,255,255,.55),rgba(255,255,255,.15));position:relative}
  .trophy::after{content:"";position:absolute;left:4px;top:6px;width:6px;height:6px;border-radius:50%;background:var(--tc)}
  .go{position:absolute;right:9px;top:17px;width:24px;height:24px;border-radius:50%;background:var(--accent);display:flex;align-items:center;justify-content:center}
  .counts{position:absolute;top:92px;left:6px;right:6px;display:flex}
  .count{flex:1;text-align:center;color:var(--text);border-right:1px solid rgba(255,255,255,.15)}
  .count:last-child{border-right:0}
  .count strong{display:block;font-size:10px;font-weight:600;line-height:1.2}
  .count small{display:block;font-size:5px;letter-spacing:.3px;color:#cde3f5}
  .date{position:absolute;top:153px;left:12px;font-size:7px;font-weight:600;color:var(--accent-soft)}
  .title{position:absolute;top:163px;left:12px;font-size:13px;font-weight:600;color:var(--text)}
  .activity{position:absolute;top:192px;left:12px;width:48px;height:218px;border-radius:24px;background:var(--panel);
    display:flex;flex-direction:column;align-items:center;justify-content:space-around;padding:6px 0}
  .metric{text-align:center;color:var(--text);width:38px}
  .metric + .metric{border-top:1px solid rgba(255,255,255,.08);padding-top:10px}
  .metric svg{display:block;margin:0 auto 4px}
  .metric strong{display:block;font-size:7px;font-weight:600;white-space:nowrap}
  .metric small{display:block;font-size:4.6px;color:var(--muted);white-space:nowrap}

  /* Muscle map area: soft bands marking upper-body and leg highlight zones */
  .muscle-map{position:absolute;left:84px;top:184px;width:126px;height:230px;border-radius:40px 40px 26px 26px;overflow:hidden}
  .muscle-map.outline{
    background:
      radial-gradient(ellipse 60% 16% at 50% 28%,var(--muscle) 0%,rgba(31,143,255,.55) 55%,transparent 100%),
      radial-gradient(ellipse 26% 24% at 50% 58%,var(--muscle) 0%,rgba(31,143,255,.5) 55%,transparent 100%),
      linear-gradient(180deg,rgba(18,70,150,.35),rgba(18,70,150,.15));
  }
  .muscle-map.silhouette{
    background:
      radial-gradient(ellipse 60% 16% at 50% 28%,var(--muscle) 0%,rgba(31,143,255,.5) 55%,transparent 100%),
      radial-gradient(ellipse 26% 24% at 50% 58%,var(--muscle) 0%,rgba(31,143,255,.45) 55%,transparent 100%),
      linear-gradient(180deg,var(--body-dark),#0a0f1c);
  }
  .nav-arrow{position:absolute;top:296px;color:var(--muted);font-size:10px}
  .nav-arrow.prev{left:70px}.nav-arrow.next{left:212px}
  .tabbar{position:absolute;left:6px;right:6px;bottom:22px;height:44px;border-radius:16px;background:var(--panel);display:flex;align-items:flex-end;padding:0 10px 7px}
  .tab{flex:1;text-align:center;color:var(--muted);font-size:5.5px}
  .tab svg{display:block;margin:0 auto 3px}
  .tab.active{color:var(--accent)}
  .tab.spacer{flex:1.2}
  .fab{position:absolute;left:50%;bottom:46px;transform:translateX(-50%);width:32px;height:32px;border-radius:50%;
    background:var(--accent);box-shadow:0 0 0 6px var(--surface),0 4px 14px rgba(30,155,255,.5);display:flex;align-items:center;justify-content:center}
  .home-bar{position:absolute;bottom:8px;left:50%;transform:translateX(-50%);width:66px;height:2.5px;border-radius:2px;background:var(--text)}
  .cta .screen{filter:blur(5px)}
  .cta .scrim{position:absolute;inset:0;background:linear-gradient(180deg,rgba(30,120,200,.25),rgba(30,140,170,.45))}
  .actions{position:absolute;right:14px;top:310px;display:flex;flex-direction:column;gap:6px}
  .action{width:114px;height:28px;border-radius:14px;background:#fff;display:flex;align-items:center;justify-content:space-between;padding:0 10px 0 12px;font-size:7px;font-weight:500;color:#1c2335;box-shadow:0 3px 10px rgba(0,0,0,.25)}
  .action i{width:10px;height:10px;border-radius:3px;background:var(--ic)}
  .cta .tabbar{background:rgba(28,35,53,.92)}
  .cta .fab{background:#fff;box-shadow:0 4px 14px rgba(0,0,0,.3)}
</style>
</head>
<body>
<main class="variants">

  <section class="variant">
    <div class="variant-label">HOME SCREEN ALT 1 - DARK</div>
    <div class="phone">
      <div class="screen">
        <div class="header"></div>
        <div class="status"><span>9:41</span><span class="status-icons"><span style="width:8px;height:5px"></span><span style="width:6px;height:5px;border-radius:3px 3px 0 0"></span><span style="width:11px;height:5px"></span></span></div>
        <div class="greeting">
          <div class="avatar" role="img" aria-label="Profile photo of Marlo"></div>
          <div class="hello">Hello, <b>Marlo</b></div>
          <div class="trophies"><div class="trophy" style="--tc:var(--green)"></div><div class="trophy" style="--tc:var(--red)"></div><div class="trophy" style="--tc:var(--purple)"></div></div>
          <div class="go"><svg width="8" height="8" viewBox="0 0 8 8"><path d="M3 1.5 5.5 4 3 6.5" stroke="#fff" stroke-width="1.2" fill="none"/></svg></div>
        </div>
        <div class="counts">
          <div class="count"><strong>38</strong><small>FOLLOWERS</small></div>
          <div class="count"><strong>4</strong><small>TROPHIES</small></div>
          <div class="count"><strong>2</strong><small>MEDALS</small></div>
          <div class="count"><strong>102</strong><small>WORKOUT</small></div>
        </div>
        <div class="date">TODAY, 24 JAN ⌄</div>
        <div class="title">Muscles Worked</div>
        <div class="activity">
          <div class="metric"><svg width="12" height="12"><circle cx="6" cy="6" r="5" fill="var(--green)"/></svg><strong>34m</strong><small>RUNNING</small></div>
          <div class="metric"><svg width="12" height="12"><circle cx="6" cy="6" r="5" fill="var(--purple)"/></svg><strong>2h 10m</strong><small>WORK OUT</small></div>
          <div class="metric"><svg width="12" height="12"><circle cx="6" cy="6" r="5" fill="var(--red)"/></svg><strong>250 kcal</strong><small>CALORIES</small></div>
        </div>
        <div class="muscle-map outline" role="img" aria-label="Outlined front-view human body diagram; shoulders, chest, arms, abs and thighs highlighted blue as worked muscle groups"></div>
        <span class="nav-arrow prev">‹</span><span class="nav-arrow next">›</span>
        <nav class="tabbar">
          <div class="tab active"><svg width="11" height="11"><rect x="1" y="1" width="9" height="9" rx="2" fill="currentColor"/></svg>Home</div>
          <div class="tab"><svg width="11" height="11"><rect x="1" y="1" width="9" height="9" rx="2" fill="currentColor"/></svg>Stats</div>
          <div class="tab spacer"></div>
          <div class="tab"><svg width="11" height="11"><circle cx="5.5" cy="5.5" r="4.5" fill="currentColor"/></svg>Profile</div>
          <div class="tab"><svg width="11" height="11"><polygon points="5.5,0.5 10,3 10,8 5.5,10.5 1,8 1,3" fill="currentColor"/></svg>Settings</div>
        </nav>
        <div class="fab"><svg width="14" height="14"><path d="M7 1v12M1 7h12" stroke="#fff" stroke-width="2"/></svg></div>
        <div class="home-bar"></div>
      </div>
    </div>
  </section>

  <section class="variant">
    <div class="variant-label">HOME SCREEN ALT 2 - DARK</div>
    <div class="phone">
      <div class="screen">
        <div class="header"></div>
        <div class="status"><span>9:41</span><span class="status-icons"><span style="width:8px;height:5px"></span><span style="width:6px;height:5px;border-radius:3px 3px 0 0"></span><span style="width:11px;height:5px"></span></span></div>
        <div class="greeting">
          <div class="avatar" role="img" aria-label="Profile photo of Marlo"></div>
          <div class="hello">Hello, <b>Marlo</b></div>
          <div class="trophies"><div class="trophy" style="--tc:var(--green)"></div><div class="trophy" style="--tc:var(--red)"></div><div class="trophy" style="--tc:var(--purple)"></div></div>
          <div class="go"><svg width="8" height="8" viewBox="0 0 8 8"><path d="M3 1.5 5.5 4 3 6.5" stroke="#fff" stroke-width="1.2" fill="none"/></svg></div>
        </div>
        <div class="counts">
          <div class="count"><strong>38</strong><small>FOLLOWERS</small></div>
          <div class="count"><strong>4</strong><small>TROPHIES</small></div>
          <div class="count"><strong>2</strong><small>MEDALS</small></div>
          <div class="count"><strong>102</strong><small>WORKOUT</small></div>
        </div>
        <div class="date">TODAY, 24 JAN ⌄</div>
        <div class="title">Muscles Worked</div>
        <div class="activity">
          <div class="metric"><svg width="12" height="12"><circle cx="6" cy="6" r="5" fill="var(--green)"/></svg><strong>34m</strong><small>RUNNING</small></div>
          <div class="metric"><svg width="12" height="12"><circle cx="6" cy="6" r="5" fill="var(--purple)"/></svg><strong>2h 10m</strong><small>WORK OUT</small></div>
          <div class="metric"><svg width="12" height="12"><circle cx="6" cy="6" r="5" fill="var(--red)"/></svg><strong>250 kcal</strong><small>CALORIES</small></div>
        </div>
        <div class="muscle-map silhouette" role="img" aria-label="Dark front-view human body silhouette; shoulders, chest, arms and thighs glowing blue as worked muscle groups"></div>
        <span class="nav-arrow prev">‹</span><span class="nav-arrow next">›</span>
        <nav class="tabbar">
          <div class="tab active"><svg width="11" height="11"><rect x="1" y="1" width="9" height="9" rx="2" fill="currentColor"/></svg>Home</div>
          <div class="tab"><svg width="11" height="11"><rect x="1" y="1" width="9" height="9" rx="2" fill="currentColor"/></svg>Stats</div>
          <div class="tab spacer"></div>
          <div class="tab"><svg width="11" height="11"><circle cx="5.5" cy="5.5" r="4.5" fill="currentColor"/></svg>Profile</div>
          <div class="tab"><svg width="11" height="11"><polygon points="5.5,0.5 10,3 10,8 5.5,10.5 1,8 1,3" fill="currentColor"/></svg>Settings</div>
        </nav>
        <div class="fab"><svg width="14" height="14"><path d="M7 1v12M1 7h12" stroke="#fff" stroke-width="2"/></svg></div>
        <div class="home-bar"></div>
      </div>
    </div>
  </section>

  <section class="variant">
    <div class="variant-label">HOME SCREEN + CTA - DARK</div>
    <div class="phone cta">
      <div class="screen">
        <div class="header"></div>
        <div class="greeting">
          <div class="avatar" role="img" aria-label="Profile photo of Marlo"></div>
          <div class="hello">Hello, <b>Marlo</b></div>
          <div class="trophies"><div class="trophy" style="--tc:var(--green)"></div><div class="trophy" style="--tc:var(--red)"></div><div class="trophy" style="--tc:var(--purple)"></div></div>
          <div class="go"></div>
        </div>
        <div class="counts">
          <div class="count"><strong>38</strong><small>FOLLOWERS</small></div>
          <div class="count"><strong>4</strong><small>TROPHIES</small></div>
          <div class="count"><strong>2</strong><small>MEDALS</small></div>
          <div class="count"><strong>102</strong><small>WORKOUT</small></div>
        </div>
        <div class="date">TODAY, 24 JAN ⌄</div>
        <div class="title">Muscles Worked</div>
        <div class="activity"></div>
        <div class="muscle-map silhouette" role="img" aria-label="Blurred body diagram behind the quick action menu"></div>
      </div>
      <div class="scrim"></div>
      <div class="actions">
        <div class="action">Strength Review<i style="--ic:var(--purple)"></i></div>
        <div class="action">Start Workout<i style="--ic:var(--green)"></i></div>
        <div class="action">Log Food<i style="--ic:var(--red)"></i></div>
      </div>
      <nav class="tabbar">
        <div class="tab"><svg width="11" height="11"><rect x="1" y="1" width="9" height="9" rx="2" fill="currentColor"/></svg>Home</div>
        <div class="tab"><svg width="11" height="11"><rect x="1" y="1" width="9" height="9" rx="2" fill="currentColor"/></svg>Stats</div>
        <div class="tab spacer"></div>
        <div class="tab"><svg width="11" height="11"><circle cx="5.5" cy="5.5" r="4.5" fill="currentColor"/></svg>Profile</div>
        <div class="tab"><svg width="11" height="11"><polygon points="5.5,0.5 10,3 10,8 5.5,10.5 1,8 1,3" fill="currentColor"/></svg>Settings</div>
      </nav>
      <div class="fab"><svg width="12" height="12"><path d="M1 1l10 10M11 1 1 11" stroke="var(--accent)" stroke-width="2"/></svg></div>
      <div class="home-bar"></div>
    </div>
  </section>

</main>
</body>
</html>
```